new private customer brochure

New brochure for advertising our services in bathroom remodeling, heating system renovation, and ventilation cleaning. Brochure size A5 with 4 pages. More informations about the company will you see on the website: www.talvenrik.ch

```html
<!DOCTYPE html>
<html lang="de">
<head>
<meta charset="utf-8">
<title>Talvenrik – Broschüre Privatkunden</title>
<link rel="stylesheet" href="https://fonts.googleapis.com/css2?family=Fredoka:wght@600&family=Outfit:wght@400;600;700&display=swap">
<style>
  :root {
    --paper: #ffffff;
    --stage: #f1f1f1;
    --ink: #1b1b1b;
    --yellow: #f6d21b;
    --blue: #3a8ed0;
    --green: #178766;
    --red: #e01e3f;
    --orange: #f0992a;
    --black: #000000;
  }
  * { margin: 0; padding: 0; box-sizing: border-box; }
  html, body { width: 983px; height: 1200px; overflow: hidden; background: var(--stage); }
  body { position: relative; font-family: "Outfit", sans-serif; color: var(--ink); }

  .spread { position: absolute; left: 115px; width: 753px; height: 533px; background: var(--paper); overflow: hidden; }
  .spread--outer { top: 63px; }
  .spread--inner { top: 625px; }
  .abs { position: absolute; }

  .heading { font-family: "Fredoka", sans-serif; font-weight: 600; }
  .body-copy { font-size: 10.5px; line-height: 1.25; }
  .body-copy p { margin-bottom: 12px; }
  .body-copy ul { list-style: none; margin-bottom: 12px; }
  .body-copy li { padding-left: 7px; text-indent: -7px; }
  .body-copy li::before { content: "• "; }

  /* outer spread – back page */
  .accent-bar { left: 0; top: 24px; width: 303px; height: 13px; background: var(--yellow); }
  .ventilation__title { left: 27px; top: 62px; font-size: 20px; line-height: 1.25; }
  .ventilation__copy { left: 27px; top: 124px; width: 310px; }

  /* outer spread – cover */
  .cover-shapes { left: 0; top: 0; }
  .brand { left: 551px; top: 30px; width: 180px; }
  .brand__name { font-family: "Fredoka", sans-serif; font-weight: 600; font-size: 25px; letter-spacing: 1px; text-transform: uppercase; line-height: 1; color: var(--ink); display: flex; align-items: center; gap: 6px; }
  .brand__dot { width: 10px; height: 10px; border-radius: 50%; background: var(--ink); }
  .brand__tag { font-size: 8.5px; letter-spacing: 0.6px; margin-top: 5px; font-weight: 600; }
  .cover-visual { left: 478px; top: 124px; width: 252px; height: 214px; border-radius: 4px;
    background: linear-gradient(160deg, #eef3f8 0%, #c9d9ea 60%, #2a6fb5 100%); }
  .cover-claim { left: 410px; top: 383px; width: 316px; text-align: center; color: #fff; }
  .cover-claim__title { font-size: 15px; line-height: 1.3; letter-spacing: 0.3px; }
  .cover-claim__list { list-style: none; margin-top: 14px; font-size: 10.5px; line-height: 1.3; }

  /* inner spread – bathroom */
  .tile { position: absolute; }
  .tile--green { left: 94px; top: 0; width: 112px; height: 113px; background: var(--green); }
  .tile--yellow-a { left: 279px; top: 0; width: 98px; height: 97px; background: var(--yellow); }
  .tile--yellow-b { left: 0; top: 80px; width: 112px; height: 97px; background: var(--yellow); }
  .tile--black { left: 189px; top: 80px; width: 112px; height: 97px; background: var(--black); }
  .bath { left: 0; top: 184px; width: 377px; height: 349px; background: var(--red); color: #fff; }
  .bath__title { position: absolute; left: 27px; top: 36px; font-size: 19px; }
  .bath__copy { position: absolute; left: 27px; top: 66px; width: 345px; font-size: 10.8px; }
  .bath__sub { font-weight: 700; font-size: 9.5px; line-height: 1.3; margin-bottom: 8px; }
  .bath__note { font-size: 8.8px; line-height: 1.35; }

  /* inner spread – heating */
  .label { left: 377px; top: 41px; width: 234px; height: 36px; background: var(--orange); padding-left: 16px; display: flex; align-items: center; font-size: 19px; }
  .heating__copy { left: 393px; top: 102px; width: 256px; font-size: 9.4px; }
  .heating__copy h3 { font-weight: 700; font-size: 10px; line-height: 1.25; margin: 4px 0 10px; text-transform: uppercase; }
  .side-bar { left: 706px; width: 47px; height: 146px; }
  .side-bar--blue { top: 123px; background: var(--blue); }
  .side-bar--yellow { top: 326px; background: var(--yellow); }
</style>
</head>
<body>

<section class="spread spread--outer">
  <div class="abs accent-bar"></div>
  <h1 class="abs heading ventilation__title">Lüftungsreinigung von<br>Kanal- und Rohrleitungen</h1>
  <div class="abs body-copy ventilation__copy">
    <p>Eine einwandfreie funktionierende Wohnungslüftungsanlage gewährleistet in den Wohnräumen kontinuierlich frische Aussenluft und die effiziente Abführung von Feuchtigkeit sowie „verbrauchter“ Luft.</p>
    <p>Ablagerungen von Viren, Pilzen, Bakterien und anderen Biomassen können in den Lüftungssystemen folgende Auswirkungen haben:</p>
    <ul>
      <li>Verursachung unangenehmer Gerüche</li>
      <li>Staub und Fett können als Brandbeschleuniger wirken</li>
      <li>Einatmen von Mikroorganismen, was zu Kopfschmerzen, Atemwegsbeschwerden, Schleimhautentzündung oder allergischen Reaktionen führen kann</li>
    </ul>
    <p>Durch regelmässigen Austausch der Luftfilter und Reinigung der Komponenten ergeben sich folgende Vorteile:</p>
    <ul>
      <li>Steigerung des Wohlbefindens und der Vitalität</li>
      <li>Reduzierung von Krankheitsausfällen</li>
      <li>Verhinderung allergischer Reaktionen</li>
      <li>Senkung der Betrieb- und Energiekosten</li>
      <li>Störungsfreier Betrieb</li>
      <li>Werterhaltung der Lüftungsanlage</li>
    </ul>
    <p>Um einen langfristig zuverlässigen und effizienten Betrieb zu gewährleisten, ist eine regelmässige Kontrolle und gegebenenfalls eine professionelle Reinigung empfehlenswert.</p>
  </div>

  <svg class="abs cover-shapes" width="753" height="533" viewBox="0 0 753 533" aria-hidden="true">
    <polygon points="377,0 377,533 753,533" fill="var(--blue)"/>
    <polygon points="551,0 753,0 753,275" fill="var(--yellow)"/>
  </svg>

  <div class="abs brand">
    <div class="brand__name"><span class="brand__dot"></span>Talvenrik</div>
    <div class="brand__tag">HAUSTECHNIK + BAUSPENGLEREI</div>
  </div>

  <div class="abs cover-visual" role="img" aria-label="Illustration eines Hauses mit Solaranlage, Heiztechnik, Lüftung und Elektroauto an der Ladestation"></div>

  <div class="abs cover-claim">
    <h2 class="heading cover-claim__title">TALVENRIK<br>Gebäude-Kompetenz</h2>
    <ul class="cover-claim__list">
      <li>Heizungsersatz</li>
      <li>Ersatz sanitäre Anlagen</li>
      <li>Lüftungsanlagenersatz</li>
      <li>Photovoltaik Anlagen</li>
      <li>Dach- und Fassade</li>
    </ul>
  </div>
</section>

<section class="spread spread--inner">
  <div class="tile tile--green"></div>
  <div class="tile tile--yellow-a"></div>
  <div class="tile tile--yellow-b"></div>
  <div class="tile tile--black"></div>

  <div class="abs bath">
    <h2 class="heading bath__title">Badumbau</h2>
    <div class="body-copy bath__copy">
      <p>Ein neues Traumbad für die eigenen vier Wände?<br>Wir bauen es für Sie innert kurzer Zeit...</p>
      <p>Im Badezimmer sind die Armaturen verkratzt, die Duschtrennwand rinnt, die Badewanne defekt oder Sie haben einfach Lust, Ihr Badezimmer neu zu gestalten? Wir unterstützen Sie bei Ihrem Badumbau von der Planung über die Beratung bis zur Ausführung.</p>
      <p>Für eine noch genauere Umsetzung Ihrer Idee, visualisieren wir für Sie eine 3D-Badgestaltung. Erleben Sie Ihr neues Badezimmer in Farbe, Form, Material und Licht noch vor dem Umbau. Mit unserer Bad-Kalkulator erhalten Sie in wenigen Schritten eine erste Kostenschätzung.</p>
      <h3 class="bath__sub">IHREN BADUMBAU PLANEN,<br>KOORDINIEREN UND REALISIEREN</h3>
      <p class="bath__note">Alles aus einer Hand. Wir planen und gestalten nach Ihren Wünschen.<br>Wir organisieren und koordinieren alle Arbeiten mit den beteiligten Fachleuten.</p>
    </div>
  </div>

  <h2 class="abs heading label">Heizungssanierung</h2>
  <div class="abs body-copy heating__copy">
    <p>Steigen die Nebenkosten Ihrer bestehenden Elektro-, Öl- oder Gasheizung jährlich an oder empfinden Sie die Umweltbelastung als zu gross?</p>
    <p>Die Möglichkeiten sind vielfältig. Für die Wahl des richtigen Heizsystems ist eine kompetente Beratung deshalb unabdingbar. Mit unserer langjährigen Erfahrung im Neu- und Umbau sind wir der ideale Partner für Ihr Projekt.</p>
    <h3>ENVALO Plus - Einheitliche Etikette bei Gebäudesanierungen</h3>
    <p>Der ENVALO gibt Aufschluss über den Energiezustand eines Gebäudes. Je nach Alter und Ausbaustandard muss Ihr Gebäude unterschiedliche Anforderungen erfüllen. Unsere ENVALO-zertifizierten Mitarbeitenden stellen Ihren Gebäudeenergieausweis ENVALO aus oder zeigen Ihnen mittels ENVALO Plus konkrete Massnahmen auf, wie Sie den energetischen Zustand Ihrer Liegenschaft verbessern können.</p>
    <h3>Profitieren Sie von attraktiven Fördergeldern</h3>
    <p>Je nach gewähltem Heizsystem und Wohnort unterstützt Sie der Kanton oder Bund mit interessanten Fördergeldern. Gerne unterstützen wir Sie bei der Beantragung.</p>
    <h3>Serviceorganisation mit<br>24h-Pikettdienst</h3>
    <p>Rund um die Uhr und während dem ganzen Jahr sind wir mit unserem Pikettdienst für Sie im Einsatz.</p>
  </div>
  <div class="abs side-bar side-bar--blue"></div>
  <div class="abs side-bar side-bar--yellow"></div>
</section>

</body>
</html>
```